Text only wordpress site to capture emails

Refer to inspiration upload for list of sites that will be useful for you.

We need a site that will be used to capture emails from clients that follow us on social media. The site will be all text, pretty simple. I have a couple of text sites that I like and we can use them for an example.

Menu section will have home, archive, about.
Footer will have © and Website Privacy Policy | Legal and Policies
There will be some text on the home page and an email capture.

This site will be all text no pictures.

I discuss Cubicle Matters so the text portions will have some questions and answers on this and then prompt for the visitor to subscribe to my email list.

The only purpose of the site is to build an email list from existing social media followers so the site will be pretty simple in and of itself.

• Text only, similar Q&A to uploaded pics.

I will use a template from mail lantern dotcom for email capture.

I like the simple couriernew font family that is on both sites supplied in the uploads.
• If you use any color it needs to be very minimal.

```html
<!DOCTYPE html>
<html lang="en">
<head>
<meta charset="utf-8">
<title>Cubicle Matters</title>
<link href="https://fonts.googleapis.com/css2?family=Courier+Prime:wght@400;700&display=swap" rel="stylesheet">
<style>
  :root {
    --ink: #111111;
    --text: #555555;
    --nav: #333333;
    --rule: #dddddd;
    --chip: #e6e6e6;
    --paper: #ffffff;
  }
  * { margin: 0; padding: 0; box-sizing: border-box; }
  html, body {
    width: 1200px;
    height: 1190px;
    overflow: hidden;
    background: var(--paper);
    font-family: "Courier Prime", "Courier New", monospace;
    color: var(--ink);
  }
  .page { position: relative; width: 1200px; height: 1190px; }

  .sidebar { position: absolute; left: 141px; top: 48px; width: 260px; }
  .site-title {
    font-size: 31px; line-height: 32px; font-weight: 400;
    letter-spacing: 0.5px; color: var(--ink);
  }
  .site-nav { margin-top: 50px; list-style: none; }
  .site-nav li { height: 37px; }
  .site-nav a {
    font-size: 14px; line-height: 20px; color: var(--nav);
    text-decoration: none; letter-spacing: 0.5px; display: inline-block;
  }
  .site-nav a.is-current {
    color: var(--ink);
    border-bottom: 1px solid var(--ink);
    padding-bottom: 2px;
  }

  .content { position: absolute; left: 451px; top: 49px; width: 640px; }
  .intro-title { font-size: 15px; line-height: 20px; font-weight: 700; letter-spacing: 0.5px; }
  .intro-text {
    margin-top: 8px; font-size: 12px; line-height: 18px;
    color: var(--text); letter-spacing: 0.4px; margin-bottom: 34px;
  }
  .qa { margin-bottom: 36px; }
  .qa-question {
    font-size: 11.5px; line-height: 16px; font-weight: 700;
    letter-spacing: 0.3px; margin-bottom: 7px;
  }
  .qa-answer {
    font-size: 12px; line-height: 18px; color: var(--text);
    letter-spacing: 0.4px; white-space: nowrap;
  }

  .site-footer {
    position: absolute; left: 141px; top: 1120px; width: 918px;
    border-top: 1px solid var(--rule);
    display: flex; justify-content: space-between; align-items: center;
    padding-top: 18px;
  }
  .legal {
    font-size: 12px; line-height: 32px; color: var(--text);
    letter-spacing: 0.4px; padding-left: 1px; white-space: nowrap; flex: none;
  }
  .legal a { color: var(--text); text-decoration: none; }
  .social { display: flex; gap: 10px; list-style: none; flex: none; }
  .social a {
    display: flex; align-items: center; gap: 4px;
    font-size: 10px; line-height: 32px; color: var(--text);
    text-decoration: none; white-space: nowrap;
  }
  .social .dot { width: 8px; height: 8px; background: var(--chip); flex: none; }
</style>
</head>
<body>
<div class="page">
  <aside class="sidebar">
    <h1 class="site-title">Cubicle<br>Matters</h1>
    <ul class="site-nav">
      <li><a href="#" class="is-current">Home</a></li>
      <li><a href="#">Archive</a></li>
      <li><a href="#">About Us</a></li>
      <li><a href="#">Subscribe</a></li>
    </ul>
  </aside>

  <main class="content">
    <h2 class="intro-title">What the...</h2>
    <p class="intro-text">Lorem ipsum dolor sit amet, consectetuer adipiscing elit.</p>

    <article class="qa">
      <h3 class="qa-question">Q:Ut wisi enim ad minim veniam, quis nostrud exerci?</h3>
      <p class="qa-answer">A:Lorem ipsum dolor sit amet, consectetuer adipiscing elit, sed diam nonummy<br>nibh euismod tincidunt ut laoreet dolore magna aliquam erat volutpat. Ut wisi<br>enim ad minim veniam, quis nostrud exerci tation.</p>
    </article>
    <article class="qa">
      <h3 class="qa-question">Q:Sed diam nonummy nibh euismod tincidunt?</h3>
      <p class="qa-answer">A:Lorem ipsum dolor sit amet, consectetuer adipiscing elit, sed diam nonummy<br>nibh euismod tincidunt ut laoreet dolore magna aliquam erat volutpat. Ut wisi<br>enim ad minim veniam, quis nostrud exerci tation.</p>
    </article>
    <article class="qa">
      <h3 class="qa-question">Q:Duis autem vel eum iriure dolor in hendrerit in vulputate?</h3>
      <p class="qa-answer">A:Lorem ipsum dolor sit amet, consectetuer adipiscing elit, sed diam nonummy<br>nibh euismod tincidunt ut laoreet dolore magna aliquam erat volutpat.</p>
    </article>
    <article class="qa">
      <h3 class="qa-question">Q:Sed diam nonummy nibh euismod tincidunt?</h3>
      <p class="qa-answer">A:Lorem ipsum dolor sit amet, consectetuer adipiscing elit, sed diam nonummy<br>nibh euismod tincidunt ut laoreet dolore magna aliquam erat volutpat. Ut wisi<br>enim ad minim veniam, quis nostrud exerci tation.</p>
    </article>
    <article class="qa">
      <h3 class="qa-question">Q:Ut wisi enim ad minim veniam, quis nostrud exerci?</h3>
      <p class="qa-answer">A:Lorem ipsum dolor sit amet, consectetuer adipiscing elit, sed diam nonummy<br>nibh euismod tincidunt ut laoreet dolore magna aliquam erat volutpat. Ut wisi<br>enim ad minim veniam, quis nostrud exerci tation.</p>
    </article>
    <article class="qa">
      <h3 class="qa-question">Q:Duis autem vel eum iriure dolor in hendrerit in vulputate?</h3>
      <p class="qa-answer">A:Lorem ipsum dolor sit amet, consectetuer adipiscing elit, sed diam nonummy<br>nibh euismod tincidunt ut laoreet dolore magna aliquam erat volutpat.</p>
    </article>
    <article class="qa">
      <h3 class="qa-question">Q:Ut wisi enim ad minim veniam, quis nostrud exerci?</h3>
      <p class="qa-answer">A:Lorem ipsum dolor sit amet, consectetuer adipiscing elit, sed diam nonummy<br>nibh euismod tincidunt ut laoreet dolore magna aliquam erat volutpat. Ut wisi<br>enim ad minim veniam, quis nostrud exerci tation.</p>
    </article>
    <article class="qa">
      <h3 class="qa-question">Q:Sed diam nonummy nibh euismod tincidunt?</h3>
      <p class="qa-answer">A:Lorem ipsum dolor sit amet, consectetuer adipiscing elit, sed diam nonummy<br>nibh euismod tincidunt ut laoreet dolore magna aliquam erat volutpat. Ut wisi<br>enim ad minim veniam, quis nostrud exerci tation.</p>
    </article>
    <article class="qa">
      <h3 class="qa-question">Q:Duis autem vel eum iriure dolor in hendrerit in vulputate?</h3>
      <p class="qa-answer">A:Lorem ipsum dolor sit amet, consectetuer adipiscing elit, sed diam nonummy<br>nibh euismod tincidunt ut laoreet dolore magna aliquam erat volutpat.</p>
    </article>
  </main>

  <footer class="site-footer">
    <p class="legal">Copyright &copy; 2021 Cubicle Matters. All Right Reserved. <a href="#">Privacy Policy</a> | <a href="#">Legal and Policies</a></p>
    <ul class="social">
      <li><a href="#"><span class="dot"></span>Friendloop</a></li>
      <li><a href="#"><span class="dot"></span>Snapframe</a></li>
      <li><a href="#"><span class="dot"></span>Chirpline</a></li>
    </ul>
  </footer>
</div>
</body>
</html>
```